KBR, LLC Original

I need a business card design for a new company in Gaithersburg, MD. Though the name of the company is Wiring By Candor (Wiring By Candor) we specialize in commercial kitchen ventilation systems as a complete turnkey project or as a service provider. We can design the entire system including the hoods, fans, ductwork, and fire system. We also specialize in fire alarm service, design, install and inspection. We are experts on any Pellmoor Units equipment including Vexa PCU, Vexa Hoods, EMS controls, Standard controls, PCU filtration and Make-up Air units with heaters and cooling. We can repair/retrofit old water wash hood systems as well. We are experts with local code requirements and upgrades.

Industry/Entity Type

Business

Contact Information for Business Card

Neil Radcott, Wiring By Candor, LLC; 240-555-0182 Cell, Ashcombe, MD 20860. Neilr@wiringbycandorco.example

```html
<!DOCTYPE html>
<html lang="en">
<head>
<meta charset="utf-8">
<title>Wiring By Candor — Business Card</title>
<link rel="stylesheet" href="https://fonts.googleapis.com/css2?family=Ubuntu:wght@400;500;700&display=swap">
<style>
  :root {
    --brand-red: #e8001c;
    --card-white: #f4f4f2;
    --ink: #3a3a3a;
    --ink-soft: #555555;
    --backdrop: #c9c9c7;
  }
  * { margin: 0; padding: 0; box-sizing: border-box; }
  html, body {
    width: 1200px;
    height: 1000px;
    overflow: hidden;
    background: var(--backdrop);
    font-family: "Ubuntu", sans-serif;
  }
  .card {
    position: absolute;
    left: 250px;
    width: 700px;
    height: 400px;
    box-shadow: 0 6px 18px rgba(0,0,0,0.18);
  }
  /* Front side */
  .card-front {
    top: 70px;
    background: var(--brand-red);
    display: flex;
    flex-direction: column;
    align-items: center;
    justify-content: center;
    gap: 26px;
  }
  .front-mark {
    width: 118px;
    height: 118px;
    background: var(--card-white);
  }
  .front-name {
    color: var(--card-white);
    font-weight: 700;
    font-size: 40px;
    letter-spacing: 3px;
    text-transform: uppercase;
  }
  /* Back side */
  .card-back {
    top: 530px;
    background: var(--card-white);
  }
  .back-brand {
    position: absolute;
    left: 40px;
    top: 66px;
    display: flex;
    flex-direction: column;
    align-items: flex-start;
    gap: 16px;
  }
  .back-mark {
    width: 200px;
    height: 200px;
    background: var(--brand-red);
  }
  .back-brand-name {
    color: var(--brand-red);
    font-weight: 700;
    font-size: 20px;
    letter-spacing: 1px;
    text-transform: uppercase;
  }
  .edge-tab {
    position: absolute;
    right: 0;
    top: 170px;
    width: 12px;
    height: 46px;
    background: var(--brand-red);
  }
  .holder {
    position: absolute;
    left: 290px;
    top: 80px;
    color: var(--ink);
  }
  .holder-name {
    font-weight: 700;
    font-size: 28px;
  }
  .holder-title {
    font-size: 20px;
    color: var(--ink-soft);
    margin-top: 2px;
  }
  .contact-list {
    position: absolute;
    left: 290px;
    top: 180px;
    list-style: none;
    color: var(--ink);
    font-size: 21px;
    line-height: 36px;
  }
  .contact-label {
    display: inline-block;
    width: 34px;
  }
</style>
</head>
<body>
  <section class="card card-front" aria-label="Business card front">
    <div class="front-mark"></div>
    <div class="front-name">Wiring By Candor</div>
  </section>

  <section class="card card-back" aria-label="Business card back">
    <div class="back-brand">
      <div class="back-mark"></div>
      <div class="back-brand-name">Wiring By Candor</div>
    </div>
    <div class="edge-tab"></div>
    <div class="holder">
      <div class="holder-name">Neil Radcott</div>
      <div class="holder-title">your title</div>
    </div>
    <ul class="contact-list">
      <li><span class="contact-label">a</span>: Ashcombe, MD 20860</li>
      <li><span class="contact-label">m</span>: 240-555-0182</li>
      <li><span class="contact-label">e</span>: neilr@wiringbycandorco.example</li>
      <li><span class="contact-label">w</span>: www.wiringbycandorco.example</li>
    </ul>
  </section>
</body>
</html>
```